Marlow Aviation Group Envelope, Letterhead, Business Card Design

I need designs for a new company letterhead, business cards, and envelopes. These designs will need to be presented using 5 different company logos for the different divisions that are managed under the Marlow Aviation Group umbrella (company names listed below). The member of FRCU logo should also be included.
- Marlow Aviation Group
- Marlow Jet Management
- Marlow Jet Charter
- Marlow Pilot Services
- Marlow Aircraft Sales
- Marlow Flight Training

Logos for the various companies are attached as well as a screen shot of the main page of our website.

```html
<!DOCTYPE html>
<html lang="en">
<head>
<meta charset="utf-8">
<title>Marlow Aviation Group – Business Card</title>
<link href="https://fonts.googleapis.com/css2?family=Montserrat:wght@300;500;700&display=swap" rel="stylesheet">
<style>
  :root {
    --backdrop: #b3b2ae;
    --brand-blue: #0061b0;
    --emboss-blue: #0a4f93;
    --ink: #111111;
    --paper: #ffffff;
  }
  * { box-sizing: border-box; margin: 0; padding: 0; }
  html, body {
    width: 1200px; height: 857px; overflow: hidden;
    background: var(--backdrop);
    font-family: "Montserrat", sans-serif;
  }
  .stage {
    position: relative; width: 1200px; height: 857px;
    display: flex; justify-content: center; align-items: center; gap: 80px;
  }
  .card {
    position: relative; width: 300px; height: 525px; overflow: hidden;
  }
  .card--front { background: var(--paper); }
  .card--back {
    background: var(--brand-blue);
    display: flex; flex-direction: column; align-items: center; justify-content: center; gap: 22px;
  }
  .front-art { position: absolute; inset: 0; }
  .jet-silhouette { position: absolute; left: 148px; top: 232px; }
  .brand-lockup {
    position: absolute; top: 78px; left: 0; right: 0; text-align: center;
    color: var(--brand-blue); font-weight: 700;
  }
  .brand-lockup__name { font-size: 42px; letter-spacing: 2px; line-height: 1; }
  .brand-lockup__sub { font-size: 13px; letter-spacing: 4px; margin-top: 6px; }
  .contact-block {
    position: absolute; left: 28px; right: 20px; top: 372px; color: var(--paper);
  }
  .contact-block__name { font-size: 18px; font-weight: 700; }
  .contact-block__title { font-size: 12px; font-weight: 500; margin-top: 3px; }
  .contact-block__rule { width: 36px; height: 2px; background: var(--paper); margin: 12px 0 12px; }
  .contact-row {
    display: flex; align-items: center; gap: 9px;
    font-size: 11px; font-weight: 300; margin-bottom: 7px;
  }
  .contact-row svg { flex: none; }
  .division { text-align: center; color: var(--emboss-blue); font-weight: 700; }
  .division__name { font-size: 32px; letter-spacing: 2px; line-height: 1; }
  .division__sub { font-size: 10px; letter-spacing: 3px; margin-top: 4px; }
  .membership { display: flex; align-items: center; gap: 8px; color: var(--emboss-blue); font-weight: 700; }
  .membership__label { font-size: 9px; }
  .membership__name { font-size: 28px; letter-spacing: 2px; }
</style>
</head>
<body>
<main class="stage">
  <section class="card card--front">
    <svg class="front-art" width="300" height="525" viewBox="0 0 300 525">
      <path d="M0,262 Q150,278 300,332 L300,525 L0,525 Z" fill="var(--brand-blue)"/>
      <path d="M0,246 Q150,262 300,318" fill="none" stroke="var(--ink)" stroke-width="6"/>
    </svg>
    <svg class="jet-silhouette" width="140" height="72" viewBox="0 0 140 72" role="img" aria-label="Black jet silhouette flying over the curve">
      <rect width="140" height="72" rx="30" fill="var(--ink)"/>
    </svg>
    <div class="brand-lockup">
      <div class="brand-lockup__name">MARLOW</div>
      <div class="brand-lockup__sub">AVIATION GROUP</div>
    </div>
    <div class="contact-block">
      <div class="contact-block__name">Daniel Hartley</div>
      <div class="contact-block__title">Development Executive Officer</div>
      <div class="contact-block__rule"></div>
      <div class="contact-row">
        <svg width="10" height="10" viewBox="0 0 10 10"><path d="M2,0.5 L4,2.5 L3,4 Q4.5,6 6,7 L7.5,6 L9.5,8 L8,9.5 Q3,9 0.5,2 Z" fill="var(--paper)"/></svg>
        <span>+874 5550 2718</span>
      </div>
      <div class="contact-row">
        <svg width="10" height="10" viewBox="0 0 10 10"><rect x="0.5" y="2" width="9" height="6.5" fill="var(--paper)"/><path d="M0.5,2 L5,5.5 L9.5,2" fill="none" stroke="var(--brand-blue)" stroke-width="0.9"/></svg>
        <span>daniel@marlowaviationgroup.com</span>
      </div>
      <div class="contact-row">
        <svg width="10" height="10" viewBox="0 0 10 10"><circle cx="5" cy="5" r="4.3" fill="none" stroke="var(--paper)" stroke-width="0.9"/><ellipse cx="5" cy="5" rx="1.8" ry="4.3" fill="none" stroke="var(--paper)" stroke-width="0.8"/><path d="M0.7,5 H9.3" stroke="var(--paper)" stroke-width="0.8"/></svg>
        <span>marlowaviationgroup.com</span>
      </div>
    </div>
  </section>

  <section class="card card--back">
    <div class="division"><div class="division__name">MARLOW</div><div class="division__sub">JET CHARTER</div></div>
    <div class="division"><div class="division__name">MARLOW</div><div class="division__sub">JET MANAGEMENT</div></div>
    <div class="division"><div class="division__name">MARLOW</div><div class="division__sub">PILOT SERVICES</div></div>
    <div class="division"><div class="division__name">MARLOW</div><div class="division__sub">AIRCRAFT SALES</div></div>
    <div class="division"><div class="division__name">MARLOW</div><div class="division__sub">FLIGHT TRAINING</div></div>
    <div class="membership">
      <span class="membership__label">member of</span>
      <span class="membership__name">FRCU</span>
    </div>
  </section>
</main>
</body>
</html>
```